Wine label for premium wine of vinery Vrbolanec.

Design Premium wine label.

The brand is called Melvara. Brand can be extended to Dorano Melvara. There
The label should be unique and high class feeling.
This is facebook lonk of the winery
https://www.pagebook.example/402918365510274/

On facebook you can see some examole of labels that are used now. Winery is called Vrbolanec, so they used letter "K" as a logo in different ways

Target Market(s)

Premium high class yet modern living traditional but also gadget fun.
I have uploaded few inspirational photos that the owner of the vinery likes. Hope it helps.

Industry/Entity Type

Vinery

Requirements
Must have
• Black, gold, silver color to be dominated. Colors that are NOT acceptable are: green, yellow, blue, purple, pink.

The name of the vinary is Vrbolanec and it should be on the front label.
Nice to have
• The size of label should fit the Grapely application screenshot frame.
Should not have
• Cheap perception of the label and brand

```html
<!DOCTYPE html>
<html lang="en">
<head>
<meta charset="utf-8">
<title>Melvara – Cabernet Sauvignon 2018 label</title>
<link rel="stylesheet" href="https://fonts.googleapis.com/css2?family=Josefin+Sans:wght@400;600&display=swap">
<style>
  :root {
    --backdrop-light: #d9d3d0;
    --backdrop-dark: #8c8380;
    --label-black: #070404;
    --gold: #c9a06a;
    --gold-deep: #7a4b2c;
    --gold-light: #ecd6a4;
    --silver: #b9b9bb;
    --silver-shadow: rgba(255, 255, 255, 0.18);
  }
  * { margin: 0; padding: 0; box-sizing: border-box; }
  html, body {
    width: 1200px;
    height: 915px;
    overflow: hidden;
  }
  body {
    background: radial-gradient(ellipse at 50% 50%, var(--backdrop-light) 0%, var(--backdrop-dark) 100%);
    position: relative;
    font-family: "Josefin Sans", sans-serif;
  }
  .wine-label {
    position: absolute;
    left: 288px;
    top: 40px;
    width: 623px;
    height: 835px;
    background: var(--label-black);
    overflow: hidden;
    box-shadow: 0 6px 24px rgba(0, 0, 0, 0.25);
  }
  .brand-name {
    position: absolute;
    left: 0;
    right: 0;
    top: 108px;
    text-align: center;
    padding-left: 20px;
    font-weight: 600;
    font-size: 60px;
    letter-spacing: 0.16em;
    color: var(--gold);
    line-height: 1;
  }
  .wine-details {
    position: absolute;
    right: 95px;
    top: 300px;
    text-align: right;
    color: var(--silver);
    text-shadow: 0 0 3px var(--silver-shadow);
  }
  .variety {
    font-weight: 600;
    font-size: 22px;
    letter-spacing: 0.06em;
    line-height: 38px;
  }
  .vintage {
    margin-top: 18px;
    font-size: 15px;
    font-weight: 600;
    letter-spacing: 0.7em;
    margin-right: -0.7em;
  }
  .producer {
    margin-top: 44px;
    font-size: 12px;
    font-weight: 600;
    letter-spacing: 0.04em;
  }
  .wave-field {
    position: absolute;
    left: 0;
    bottom: 0;
    width: 623px;
    height: 330px;
  }
</style>
</head>
<body>
  <main class="wine-label">
    <h1 class="brand-name">MELVARA</h1>
    <section class="wine-details">
      <p class="variety">CABERNET<br>SAUVIGNON</p>
      <p class="vintage">2018</p>
      <p class="producer">VINARIJA VRBOLANEC</p>
    </section>
    <svg class="wave-field" viewBox="0 0 623 330" role="img" aria-label="Flowing gold and copper wave-line pattern across the lower label">
      <defs>
        <linearGradient id="waveTone" x1="0" y1="0" x2="1" y2="0.3">
          <stop offset="0" stop-color="#6b3f27"/>
          <stop offset="0.4" stop-color="#b38a5c"/>
          <stop offset="0.7" stop-color="#8a6038"/>
          <stop offset="1" stop-color="#c9a060"/>
        </linearGradient>
      </defs>
      <path d="M0 100 C60 90 110 105 160 80 C230 45 300 60 380 40 C460 20 540 0 623 5 L623 330 L0 330 Z" fill="url(#waveTone)"/>
    </svg>
  </main>
</body>
</html>
```